business card for LWR pty ltd

We require a business card that stands out . I have included our company flyer and would like the services listed to be put on the card so when we Give out the cards to customers they have an idea of services we provide. need the winning design to be in editable photo shop format, editable iMac pages format or editable windows publisher format, so that I can enter in names, email addresses, phone numbers etc myself. I have included a pdf documents of info / items needed on the card to use as reference please.
Updates

need more submissions

Need extra days to review

Sick

Target Market(s)

new customers

Contact Information for Business Card

details are on attached business card requirements file

Requirements
Must have
• I have attached a list of must haves

```html
<!DOCTYPE html>
<html lang="en">
<head>
<meta charset="utf-8">
<title>LWR pty ltd – Business Card</title>
<link href="https://fonts.googleapis.com/css2?family=Lato:wght@400;700&family=Montserrat:wght@800&display=swap" rel="stylesheet">
<style>
  :root {
    --page-bg: #2a2a2a;
    --card-black: #050505;
    --panel-black: #000000;
    --mesh-dark: #1c1c1c;
    --mesh-light: #3a3a3a;
    --silver: #cfcfcf;
    --white: #ffffff;
    --gold: #c8964e;
    --tab-grey: #5b5b5b;
    --earth: #b9784a;
    --earth-dark: #6b4028;
    --sky: #8fb0cc;
  }
  * { margin: 0; padding: 0; box-sizing: border-box; }
  html, body { width: 1200px; height: 1200px; overflow: hidden; background: var(--page-bg); }
  body { position: relative; font-family: "Lato", sans-serif; color: var(--white); }

  .card {
    position: absolute; left: 170px; width: 860px; height: 526px;
    border-radius: 30px; overflow: hidden; background: var(--card-black);
    box-shadow: 0 18px 40px rgba(0,0,0,.55);
  }
  .card--services { top: 50px; }
  .card--contact { top: 624px; }

  /* services side */
  .mesh-area {
    position: absolute; left: 0; top: 0; width: 860px; height: 300px;
    background: radial-gradient(ellipse at 35% 30%, var(--mesh-light), var(--mesh-dark) 55%, var(--card-black) 85%);
  }
  .brand-name {
    position: absolute; font-family: "Montserrat", sans-serif; font-weight: 800;
    color: var(--silver); letter-spacing: 4px; line-height: 1;
  }
  .card--services .brand-name { left: 230px; top: 38px; font-size: 100px; }
  .photo { position: absolute; }
  .photo--roadtrain {
    left: 130px; top: 160px; width: 730px; height: 170px;
    background: linear-gradient(180deg, #3b3025 0%, var(--earth) 45%, var(--earth-dark) 100%);
  }
  .photo--lowloader {
    left: 150px; top: 330px; width: 350px; height: 170px;
    background: linear-gradient(180deg, var(--sky) 0%, #d9dde0 50%, #7a6e62 100%);
  }
  .photo--trucks {
    left: 712px; top: 262px; width: 148px; height: 170px;
    background: linear-gradient(180deg, #0e0e0e 0%, #8a8d90 55%, #2a2520 100%);
  }
  .divider { position: absolute; width: 4px; background: var(--gold); }
  .divider--left { left: 500px; top: 300px; height: 226px; }
  .divider--right { left: 706px; top: 262px; height: 170px; }

  .services-panel {
    position: absolute; left: 504px; top: 262px; width: 202px; height: 264px;
    background: var(--panel-black);
  }
  .services-tab {
    position: absolute; left: 12px; top: 10px; width: 176px; height: 30px;
    background: var(--tab-grey); color: var(--white);
    font-size: 17px; font-weight: 700; text-align: center; line-height: 30px;
  }
  .services-list { position: absolute; left: 14px; top: 50px; list-style: none; }
  .services-list li {
    font-size: 10.5px; line-height: 15.5px; white-space: nowrap; padding-left: 12px; position: relative;
  }
  .services-list li::before {
    content: ""; position: absolute; left: 0; top: 5px; width: 6px; height: 6px;
    border-radius: 50%; background: var(--gold);
  }

  /* contact side */
  .swoosh { position: absolute; inset: 0; }
  .card--contact .brand-name { left: 540px; top: 170px; font-size: 100px; }
  .person { position: absolute; left: 70px; top: 250px; }
  .person-name { font-family: "Montserrat", sans-serif; font-weight: 800; font-size: 30px; letter-spacing: 2px; }
  .person-role { font-size: 20px; margin-top: 2px; }
  .address { margin-top: 22px; font-size: 20px; line-height: 25px; padding-left: 36px; }
  .contacts { list-style: none; margin-top: 22px; padding-left: 50px; }
  .contacts li { display: flex; align-items: center; gap: 12px; font-size: 20px; line-height: 28px; }
  .contacts svg { width: 16px; height: 16px; fill: var(--white); flex: none; }
</style>
</head>
<body>

<section class="card card--services" aria-label="Services side">
  <div class="mesh-area" role="img" aria-label="Dark metal mesh texture"></div>
  <div class="photo photo--roadtrain" role="img" aria-label="Road train of tipper trailers on an outback dirt road"></div>
  <div class="brand-name">LWR</div>
  <div class="photo photo--lowloader" role="img" aria-label="White prime mover hauling a loader on a drop deck trailer"></div>
  <div class="photo photo--trucks" role="img" aria-label="Two prime movers parked at night"></div>
  <div class="divider divider--left"></div>
  <div class="divider divider--right"></div>
  <div class="services-panel">
    <div class="services-tab">Our Services</div>
    <ul class="services-list">
      <li>Over size loads/Hot Shot Loads</li>
      <li>Heavy Vehicle Recovery Services</li>
      <li>Potable Water Deliveries</li>
      <li>Road building/Maintenance</li>
      <li>Earthworks</li>
      <li>Sand &amp; Metal Supply &amp; Cartage</li>
      <li>Road Train Tippers</li>
      <li>Road Train Tankers</li>
      <li>Road Train TFlate Tops</li>
      <li>Drop Deck Trailers</li>
      <li>Mine Site accredited</li>
      <li>Equipment &amp; Operator</li>
    </ul>
  </div>
</section>

<section class="card card--contact" aria-label="Contact side">
  <svg class="swoosh" viewBox="0 0 860 526" aria-hidden="true">
    <defs>
      <radialGradient id="meshGlow" cx="0.68" cy="0.35" r="0.45">
        <stop offset="0" stop-color="#3c3c3c"/>
        <stop offset="0.6" stop-color="#1a1a1a"/>
        <stop offset="1" stop-color="#050505"/>
      </radialGradient>
      <linearGradient id="arcShine" x1="0" y1="0" x2="1" y2="1">
        <stop offset="0" stop-color="#111"/>
        <stop offset="0.5" stop-color="#9a9a9a"/>
        <stop offset="1" stop-color="#111"/>
      </linearGradient>
    </defs>
    <path d="M430 0 C420 200 560 420 860 470 L860 0 Z" fill="url(#meshGlow)"/>
    <path d="M430 0 C420 200 560 420 860 470" fill="none" stroke="url(#arcShine)" stroke-width="8"/>
    <path d="M410 0 C400 210 545 440 860 490" fill="none" stroke="#2a2a2a" stroke-width="3"/>
  </svg>
  <div class="brand-name">LWR</div>
  <div class="person">
    <div class="person-name">DANIEL HARROW</div>
    <div class="person-role">Director</div>
    <div class="address">Lot 17 Kestrel Road<br>Australia</div>
    <ul class="contacts">
      <li><svg viewBox="0 0 16 16"><path d="M3 1l3 3-2 2c1 2 3 4 5 5l2-2 3 3-2 3C6 15 1 10 1 3z"/></svg>000 718 263</li>
      <li><svg viewBox="0 0 16 16"><path d="M1 3h14v10H1z M2 4l6 5 6-5" fill="none" stroke="#fff" stroke-width="1.6"/></svg>email@lwrservices.com.au</li>
      <li><svg viewBox="0 0 16 16"><circle cx="8" cy="8" r="6.5" fill="none" stroke="#fff" stroke-width="1.6"/><path d="M1.5 8h13M8 1.5c-3 3-3 10 0 13M8 1.5c3 3 3 10 0 13" fill="none" stroke="#fff" stroke-width="1.2"/></svg>www.lwrtransport.com.au</li>
    </ul>
  </div>
</section>

</body>
</html>
```